We are in search of a new business card design for our business. We have a Mexican Grocery Store called Tortilla Grove Market, we would like to see that some have mexican design, but we are open to any type of designs.

Phone: to be announced
Fax: to be announced

Address is:
2415 Calloway Blvd
Millbrook, MD 21290

```html
<!DOCTYPE html>
<html lang="en">
<head>
<meta charset="utf-8">
<title>Tortilla Grove Market – Business Card</title>
<link rel="stylesheet" href="https://fonts.googleapis.com/css2?family=Arimo:wght@400;700&display=swap">
<style>
  :root {
    --backdrop-top: #9a9a9a;
    --backdrop-bottom: #d8d8d8;
    --card-light: #f4f4f4;
    --card-dark: #121212;
    --ink-dark: #1a1a1a;
    --ink-light: #e6e6e6;
    --ink-muted: #a8a8a8;
  }
  * { margin: 0; padding: 0; box-sizing: border-box; }
  html, body { width: 1200px; height: 1200px; overflow: hidden; }
  body {
    background: linear-gradient(180deg, var(--backdrop-top), var(--backdrop-bottom));
    font-family: "Arimo", Arial, sans-serif;
    display: flex; align-items: center; justify-content: center;
  }
  .business-card {
    width: 1000px; height: 572px;
    display: flex;
    box-shadow: 0 18px 40px rgba(0,0,0,.28);
  }
  .brand-panel {
    width: 35%;
    background: var(--card-light);
    display: flex; flex-direction: column; align-items: center; justify-content: center;
    gap: 18px;
    padding: 0 30px;
  }
  .brand-dot {
    width: 70px; height: 70px; border-radius: 50%;
    background: var(--ink-dark);
  }
  .brand-name {
    color: var(--ink-dark);
    font-weight: 700;
    font-size: 34px;
    line-height: 1.15;
    text-align: center;
  }
  .info-panel {
    flex: 1;
    background: var(--card-dark);
    padding: 64px 56px 0 56px;
    display: flex; flex-direction: column;
  }
  .person-name { color: var(--ink-light); font-size: 34px; font-weight: 400; }
  .person-title { color: var(--ink-muted); font-size: 19px; margin-top: 4px; }
  .contact-list { list-style: none; margin-top: 150px; display: flex; flex-direction: column; gap: 14px; }
  .contact-item { display: flex; align-items: center; gap: 16px; color: var(--ink-light); font-size: 22px; }
  .contact-icon { width: 24px; height: 24px; flex: none; }
</style>
</head>
<body>
  <div class="business-card">
    <section class="brand-panel">
      <div class="brand-dot"></div>
      <div class="brand-name">Tortilla Grove<br>Market</div>
    </section>
    <section class="info-panel">
      <h1 class="person-name">Marisol Vega</h1>
      <p class="person-title">Owner</p>
      <ul class="contact-list">
        <li class="contact-item">
          <svg class="contact-icon" viewBox="0 0 24 24" aria-hidden="true">
            <rect width="24" height="24" rx="3" fill="#e6e6e6"/>
            <path d="M8 5l3 3-2 2c1 2 3 4 5 5l2-2 3 3-2 3c-6 0-12-6-12-12z" fill="#121212"/>
          </svg>
          <span>410.555.0142</span>
        </li>
        <li class="contact-item">
          <svg class="contact-icon" viewBox="0 0 24 24" aria-hidden="true">
            <rect width="24" height="24" rx="3" fill="#e6e6e6"/>
            <rect x="8" y="5" width="8" height="5" fill="#121212"/>
            <rect x="5" y="10" width="14" height="7" rx="1" fill="#121212"/>
            <rect x="8" y="15" width="8" height="4" fill="#e6e6e6" stroke="#121212" stroke-width="1.2"/>
          </svg>
          <span>410-555-0187</span>
        </li>
        <li class="contact-item">
          <svg class="contact-icon" viewBox="0 0 24 24" aria-hidden="true">
            <rect width="24" height="24" rx="3" fill="#e6e6e6"/>
            <path d="M12 4a5 5 0 0 0-5 5c0 4 5 11 5 11s5-7 5-11a5 5 0 0 0-5-5z" fill="#121212"/>
            <circle cx="12" cy="9" r="2" fill="#e6e6e6"/>
          </svg>
          <span>2415 Calloway Blvd Millbrook, MD 21290</span>
        </li>
      </ul>
    </section>
  </div>
</body>
</html>
```